Northgate Roofing Works Inc Business cards

Commercial and Residential Roofing contractor needs design logo and card design. Can be single or double sided but must incorporate:
Persons Name:
Persons Title:
Mailing Address: PO Box 3719
Physical Address: 58 Fenwick Lane
Ashby, Ma. 01431
800-316-5842
508-712-5842
Fax: 508-712-5867
Cell: Person Cell number
email address
Website: WWW.northgateroofworks.com

Target Market(s)

Residential home owners and commercial building owners

Industry/Entity Type

Roofing

Contact Information for Business Card

Persons Name:
Persons Title:
Ashby, Ma. 01431
800-316-5842
508-712-5842
Fax: 508-712-5867
Cell: Person Cell number
email address

Logo Text

Large enough to service small enough to care

Font styles to use
Serif

Colors
0355a3

Requirements
Must have
• Commercial and Residential Roofing contractor needs design logo and card design. Can be single or double sided but must incorporate:
• Persons Name:
• Persons Title:
• Mailing Address: PO Box 3719
• Physical Address: 58 Fenwick Lane
• Ashby, Ma. 01431
• 800-316-5842
• 508-712-5842
• Fax: 508-712-5867
• Cell: Person Cell number
• email address
• Website: WWW.northgateroofworks.com
Nice to have
• ..
Should not have
• I'm looking for something different. I have had the same card for 23 years. I attached what both sides of my present card looks like.

```html
<!DOCTYPE html>
<html lang="en">
<head>
<meta charset="utf-8">
<title>Northgate Roofing Works Inc – Business Cards</title>
<link rel="stylesheet" href="https://fonts.googleapis.com/css2?family=Lato:wght@300;400;700&family=Montserrat:wght@600&display=swap">
<style>
  :root {
    --bg: #d8d8d9;
    --navy: #1b202a;
    --blue-light: #35a0da;
    --blue-deep: #0355a3;
    --blue-brand: #0355a3;
    --gray-band: #9c9da0;
    --paper: #f3f4f6;
    --text-dark: #22252b;
    --white: #ffffff;
    --ink: #0f1216;
  }
  html, body {
    margin: 0;
    padding: 0;
    width: 1200px;
    height: 900px;
    overflow: hidden;
    background: var(--bg);
  }
  .canvas {
    position: relative;
    width: 1200px;
    height: 900px;
  }
  .card {
    position: absolute;
    width: 700px;
    height: 400px;
    transform: scale(0.8);
    transform-origin: 0 0;
    background: var(--navy);
    overflow: hidden;
  }
  .card--front { left: 271px; top: 88px; }
  .card--back  { left: 272px; top: 454px; }
  .card__shapes {
    position: absolute;
    inset: 0;
    width: 700px;
    height: 400px;
  }
  .brand {
    position: absolute;
    display: flex;
    align-items: center;
  }
  .brand__square {
    background: var(--blue-brand);
    flex: none;
  }
  .brand__name {
    font-family: "Montserrat", sans-serif;
    font-weight: 600;
    color: var(--white);
    line-height: 1.15;
    white-space: nowrap;
  }
  .card--front .brand { left: 150px; top: 58px; gap: 26px; }
  .card--front .brand__square { width: 78px; height: 78px; }
  .card--front .brand__name { font-size: 40px; }

  .card--back .brand { left: 360px; top: 18px; gap: 20px; }
  .card--back .brand__square { width: 62px; height: 62px; }
  .card--back .brand__name { font-size: 29px; }

  .website {
    position: absolute;
    font-family: "Lato", sans-serif;
    font-weight: 300;
    color: var(--white);
    white-space: nowrap;
  }
  .card--front .website {
    left: 0; right: 0;
    top: 362px;
    text-align: center;
    font-size: 21px;
    letter-spacing: 0.2em;
  }
  .card--back .website {
    left: 360px;
    top: 96px;
    font-size: 15px;
    letter-spacing: 0.22em;
  }
  .person {
    position: absolute;
    left: 20px;
    top: 106px;
    font-family: "Lato", sans-serif;
    font-weight: 700;
    font-size: 20px;
    line-height: 24px;
    color: var(--white);
  }
  .person__title { font-weight: 400; }
  .contact {
    position: absolute;
    font-family: "Lato", sans-serif;
    font-weight: 700;
    font-size: 16px;
    line-height: 20px;
    color: var(--text-dark);
    margin: 0;
    padding: 0;
    list-style: none;
  }
  .contact--lines { left: 104px; top: 253px; }
  .contact--address { left: 364px; top: 249px; }
  .contact li {
    position: relative;
    padding-left: 26px;
    white-space: nowrap;
  }
  .contact .icon {
    position: absolute;
    left: 0;
    top: 3px;
    width: 16px;
    height: 16px;
  }
</style>
</head>
<body>
<div class="canvas">

  <section class="card card--front" aria-label="Card front">
    <svg class="card__shapes" viewBox="0 0 700 400" aria-hidden="true">
      <defs>
        <linearGradient id="bandFront" x1="0" y1="0" x2="1" y2="0">
          <stop offset="0" stop-color="var(--blue-light)"/>
          <stop offset="1" stop-color="var(--blue-deep)"/>
        </linearGradient>
      </defs>
      <polygon fill="url(#bandFront)" points="0,250 700,172 700,216 0,300"/>
      <polygon fill="var(--gray-band)" points="0,312 700,228 700,240 0,325"/>
    </svg>
    <div class="brand">
      <span class="brand__square"></span>
      <span class="brand__name">Northgate<br>Roofing Works</span>
    </div>
    <div class="website">www.northgateroofworks.com</div>
  </section>

  <section class="card card--back" aria-label="Card back">
    <svg class="card__shapes" viewBox="0 0 700 400" aria-hidden="true">
      <defs>
        <linearGradient id="bandBack" x1="0" y1="0" x2="1" y2="0">
          <stop offset="0" stop-color="var(--blue-light)"/>
          <stop offset="1" stop-color="var(--blue-deep)"/>
        </linearGradient>
      </defs>
      <polygon fill="url(#bandBack)" points="0,92 700,166 700,206 0,164"/>
      <polygon fill="var(--gray-band)" points="0,176 700,216 700,226 0,188"/>
      <polygon fill="var(--paper)" points="0,200 700,240 700,388 0,388"/>
      <rect fill="var(--ink)" x="0" y="388" width="700" height="12"/>
    </svg>
    <div class="brand">
      <span class="brand__square"></span>
      <span class="brand__name">Northgate<br>Roofing Works</span>
    </div>
    <div class="website">www.northgateroofworks.com</div>
    <div class="person">
      <div class="person__name">Dana R. Whitcombe</div>
      <div class="person__title">CEO</div>
    </div>
    <ul class="contact contact--lines">
      <li>
        <svg class="icon" viewBox="0 0 16 16" aria-hidden="true"><path fill="var(--blue-brand)" d="M3.2 1.5l2.3 2.6-1.3 1.6c.8 2 2.3 3.5 4.2 4.3l1.6-1.3 2.6 2.3-1.2 2.3C6.3 13.1 2.6 9.4 1 4.4z"/></svg>
        800-316-5842<br>508-712-5842
      </li>
      <li>
        <svg class="icon" viewBox="0 0 16 16" aria-hidden="true"><path fill="var(--blue-brand)" d="M4 1h8v4H4zM1 6h14v6h-3v3H4v-3H1zm4 4v4h6v-4z"/></svg>
        508-712-5867
      </li>
      <li>
        <svg class="icon" viewBox="0 0 16 16" aria-hidden="true"><rect x="4" y="1" width="8" height="14" rx="1.5" fill="none" stroke="var(--blue-brand)" stroke-width="2" transform="rotate(15 8 8)"/></svg>
        0147-258-369
      </li>
      <li>
        <svg class="icon" viewBox="0 0 16 16" aria-hidden="true"><rect x="1" y="3" width="14" height="10" fill="none" stroke="var(--blue-brand)" stroke-width="1.4"/><path d="M1 3l7 6 7-6" fill="none" stroke="var(--blue-brand)" stroke-width="1.4"/></svg>
        dana_whitcombe@northgateroofworks.com
      </li>
    </ul>
    <ul class="contact contact--address">
      <li>
        <svg class="icon" viewBox="0 0 16 16" aria-hidden="true"><path fill="var(--blue-brand)" d="M8 0a5 5 0 0 0-5 5c0 3.5 5 8.5 5 8.5s5-5 5-8.5a5 5 0 0 0-5-5zm0 7a2 2 0 1 1 0-4 2 2 0 0 1 0 4z"/><rect x="2" y="14.5" width="12" height="1.5" fill="var(--blue-brand)"/></svg>
        PO Box 3719<br>58 Fenwick Lane Ashby,<br>Ma. 01431
      </li>
    </ul>
  </section>

</div>
</body>
</html>
```